Business Card Design Project - IT Company

CLOUD IT company working with medium to large corporate clients requires 2 sided Business Card design.

Strong, Professional and modern is what I am looking for.

The Logo JPG attached has all the colour palette options. which consist of Red and Silver on various backgrounds

Preferred option for the Back of card is either Silver Text on Red or Silver Text on Black. Though this is not concrete. Surprise me.

Logo must be prominent along with Contact details of the staff member

Tagline can be all Capitals " CLOUD MANAGED SERVICES"

I will look to provide feedback and tweaks to get the right design so it should be a fun process.

I will provide the layered files to the top few contenders.

Reason: Leaving the door open for some creativity. Don't forget this is an technology company. .

Target Market(s)

Leaders, decision makers, CEOs, CIOs,

Industry/Entity Type

Business

Requirements
Must have
• Data must have is

Company Name: Brelquist
Tagline: Cloud Managed Services

No Particular order

First Name Last name
Director
Mobile 0477 555 019
www.brelquist-example.com
First.Lastname@brelquist-example.com
Suite 7, 48 Wexmoor Lane, Sydney NSW 2000

```html
<!DOCTYPE html>
<html lang="en">
<head>
<meta charset="utf-8">
<title>Brelquist – Business Card</title>
<link rel="stylesheet" href="https://fonts.googleapis.com/css2?family=Jost:wght@300;400;500;600&display=swap">
<style>
  :root {
    --backdrop: #1f1f1f;
    --card: #ffffff;
    --red: #a3212a;
    --red-light: #b93a40;
    --red-dark: #8c1a22;
    --ink: #2b2b2b;
    --silver: #5a5a5a;
    --white: #ffffff;
  }
  * { margin: 0; padding: 0; box-sizing: border-box; }
  html, body {
    width: 1200px; height: 900px; overflow: hidden;
    background: var(--backdrop);
    font-family: "Jost", "Futura", sans-serif;
  }
  .stage { position: relative; width: 1200px; height: 900px; }

  .card {
    position: absolute; left: 323px; width: 586px; height: 360px;
    background: var(--card);
  }
  .card--front { top: 58px; }
  .card--back { top: 467px; }

  /* front */
  .tab { position: absolute; background: var(--red); border-radius: 2px; }
  .tab--top { left: 10px; top: 0; width: 149px; height: 8px; }
  .tab--bottom { left: 10px; bottom: 0; width: 149px; height: 8px; }

  .side-brand {
    position: absolute; left: 0; top: 8px; width: 168px; height: 344px;
  }
  .side-brand__lockup {
    position: absolute; left: 84px; top: 150px;
    transform: translate(-50%, -50%) rotate(-90deg);
    text-align: left; white-space: nowrap;
  }
  .side-brand__name {
    font-size: 46px; font-weight: 600; color: var(--ink); line-height: 1;
  }
  .side-brand__tagline {
    font-size: 11px; font-weight: 500; color: var(--silver);
    letter-spacing: 0.5px; margin-top: 2px;
  }
  .side-brand__dot {
    position: absolute; left: 62px; top: 272px;
    width: 44px; height: 44px; border-radius: 50%; background: var(--red);
  }

  .info-panel {
    position: absolute; left: 168px; top: 9px; width: 417px; height: 343px;
    background: radial-gradient(ellipse at 55% 10%, var(--red-light) 0%, var(--red) 55%, var(--red-dark) 100%);
    color: var(--white);
  }
  .info-panel__name {
    position: absolute; left: 0; right: 0; top: 40px; text-align: center;
    font-size: 44px; font-weight: 400; padding-left: 10px;
  }
  .info-panel__tagline {
    position: absolute; left: 0; right: 0; top: 113px; text-align: center;
    font-size: 19px; font-weight: 300; padding-left: 10px;
  }
  .staff {
    position: absolute; left: 212px; top: 162px; font-weight: 300;
  }
  .staff__name { font-size: 16px; }
  .staff__role { font-size: 15px; font-weight: 600; margin-top: 2px; }
  .staff__address { font-size: 14px; line-height: 18px; margin-top: 2px; }
  .contact {
    display: flex; align-items: center; gap: 7px; font-size: 13px; font-weight: 300;
    white-space: nowrap;
  }
  .contact svg { width: 14px; height: 14px; flex: none; }
  .staff .contact { margin-top: 9px; }
  .info-panel .contact-row {
    position: absolute; left: 42px; right: 24px; top: 306px;
    display: flex; justify-content: space-between;
  }

  /* back */
  .edge-bar {
    position: absolute; top: 8px; width: 10px; height: 345px; background: var(--red);
    border-radius: 2px;
  }
  .edge-bar--left { left: 0; }
  .edge-bar--right { right: 0; }
  .site-tab {
    position: absolute; left: 355px; top: 0; width: 190px; height: 55px;
    background: var(--red); border-radius: 0 0 4px 4px;
    color: var(--white); font-size: 15px; font-weight: 600;
    white-space: nowrap;
    display: flex; align-items: center; justify-content: center;
  }
  .main-brand {
    position: absolute; left: 60px; top: 122px; width: 470px; height: 90px;
  }
  .main-brand__dot {
    position: absolute; left: 0; top: 10px; width: 72px; height: 72px;
    border-radius: 50%; background: var(--red);
  }
  .main-brand__name {
    position: absolute; left: 110px; top: -8px;
    font-size: 72px; font-weight: 600; color: var(--ink); line-height: 1;
  }
  .main-brand__tagline {
    position: absolute; left: 200px; top: 69px;
    font-size: 16px; font-weight: 500; color: var(--silver); letter-spacing: 1px;
    white-space: nowrap;
  }
  .back-contacts {
    position: absolute; left: 44px; right: 28px; top: 280px;
    display: flex; justify-content: space-between; color: var(--red);
  }
  .back-contacts .contact { font-weight: 400; font-size: 13px; gap: 6px; }
</style>
</head>
<body>
<div class="stage">

  <section class="card card--front" aria-label="Card front">
    <div class="tab tab--top"></div>
    <div class="tab tab--bottom"></div>

    <div class="side-brand">
      <div class="side-brand__lockup">
        <div class="side-brand__name">Brelquist</div>
        <div class="side-brand__tagline">CLOUD MANAGED SERVICES</div>
      </div>
      <div class="side-brand__dot"></div>
    </div>

    <div class="info-panel">
      <div class="info-panel__name">Brelquist</div>
      <div class="info-panel__tagline">CLOUD MANAGED SERVICE</div>

      <div class="staff">
        <div class="staff__name">Mara Fenwick</div>
        <div class="staff__role">Director</div>
        <div class="staff__address">Suite 7, 48 Wexmoor Lane,<br>Sydney NSW 2000</div>
        <div class="contact">
          <svg viewBox="0 0 24 24" fill="currentColor"><path d="M19 18H6a4 4 0 0 1-.6-8 6 6 0 0 1 11.5-1.5A4.8 4.8 0 0 1 19 18z"/><path d="M12 9l-3.5 4H11v3h2v-3h2.5z" fill="#a3212a"/></svg>
          <span>www.brelquist-example.com</span>
        </div>
      </div>

      <div class="contact-row">
        <div class="contact">
          <svg viewBox="0 0 24 24" fill="currentColor"><path d="M6.6 10.8a15 15 0 0 0 6.6 6.6l2.2-2.2a1 1 0 0 1 1-.3 11 11 0 0 0 3.6.6 1 1 0 0 1 1 1V20a1 1 0 0 1-1 1A17 17 0 0 1 3 4a1 1 0 0 1 1-1h3.5a1 1 0 0 1 1 1 11 11 0 0 0 .6 3.6 1 1 0 0 1-.3 1z"/></svg>
          <span>0477 555 019</span>
        </div>
        <div class="contact">
          <svg viewBox="0 0 24 24" fill="currentColor"><path d="M2 5h20v14H2z"/><path d="M2 5l10 8 10-8" fill="none" stroke="#a3212a" stroke-width="2"/></svg>
          <span>m.fenwick@brelquist-example.com</span>
        </div>
      </div>
    </div>
  </section>

  <section class="card card--back" aria-label="Card back">
    <div class="edge-bar edge-bar--left"></div>
    <div class="edge-bar edge-bar--right"></div>
    <div class="site-tab">Brelquist-example.com</div>

    <div class="main-brand">
      <div class="main-brand__dot"></div>
      <div class="main-brand__name">Brelquist</div>
      <div class="main-brand__tagline">CLOUD MANAGED SERVICES</div>
    </div>

    <div class="back-contacts">
      <div class="contact">
        <svg viewBox="0 0 24 24" fill="currentColor"><path d="M6.6 10.8a15 15 0 0 0 6.6 6.6l2.2-2.2a1 1 0 0 1 1-.3 11 11 0 0 0 3.6.6 1 1 0 0 1 1 1V20a1 1 0 0 1-1 1A17 17 0 0 1 3 4a1 1 0 0 1 1-1h3.5a1 1 0 0 1 1 1 11 11 0 0 0 .6 3.6 1 1 0 0 1-.3 1z"/></svg>
        <span>0477 555 019</span>
      </div>
      <div class="contact">
        <svg viewBox="0 0 24 24" fill="currentColor"><path d="M19 18H6a4 4 0 0 1-.6-8 6 6 0 0 1 11.5-1.5A4.8 4.8 0 0 1 19 18z"/><path d="M12 9l-3.5 4H11v3h2v-3h2.5z" fill="#ffffff"/></svg>
        <span>www.brelquist-example.com</span>
      </div>
      <div class="contact">
        <svg viewBox="0 0 24 24" fill="currentColor"><path d="M2 5h20v14H2z"/><path d="M2 5l10 8 10-8" fill="none" stroke="#ffffff" stroke-width="2"/></svg>
        <span>m.fenwick@brelquist-example.com</span>
      </div>
    </div>
  </section>

</div>
</body>
</html>
```